Branded Flyer Template Libraries Brightmoor Funding

Create one-page flyer templates for equipment finance industry to provide a fast turnaround that consistent on-brand for educational and promotional flyers that can be quickly customized with partners logos. These will become a standard toolkit for marketing for use in Adobe Illustrator and editable. customer facing are business owners considering equipment financing typically used for leave behind flyers, email, and handouts. vendor facing to equipment dealers, manufacturers and sales reps who refer customers to us, typically used at trade shows, co branded flyers, and email promotions.
Requesting 1-2 flyer templates with concepts for educational, and promotional.
Brand guide and current flyers in circulation are uploaded as reference.
Look and feel
Each slider illustrates characteristics of the customer's brand and the style your logo design should communicate.

```html
<!DOCTYPE html>
<html lang="en">
<head>
<meta charset="utf-8">
<title>Brightmoor Funding – Flyer Templates</title>
<link rel="stylesheet" href="https://fonts.googleapis.com/css2?family=Rubik:wght@500;700;800&family=Poppins:wght@400;500&display=swap">
<style>
  :root {
    --green-dark: #0f4a1e;
    --green-light: #a2c767;
    --green-pale: #eef4e1;
    --ink: #1f3a24;
    --ink-soft: #3d4a3f;
    --stage: #c4c4c2;
    --white: #ffffff;
  }
  * { box-sizing: border-box; margin: 0; padding: 0; }
  html, body { width: 828px; height: 1200px; overflow: hidden; background: var(--stage); }
  body { position: relative; font-family: "Poppins", sans-serif; color: var(--ink); }

  .flyer {
    position: absolute; top: 324px; width: 675px; height: 955px;
    background: var(--white); overflow: hidden;
    transform: scale(0.5778); transform-origin: top left;
    box-shadow: 0 8px 24px rgba(0,0,0,.25);
  }
  .flyer--harvest { left: 16px; }
  .flyer--office { left: 422px; }

  .hero-photo { position: absolute; left: 0; top: 80px; width: 675px; height: 365px; }
  .hero-photo--field { background: linear-gradient(180deg, #c9d6cf 0%, #6e8a45 30%, #8a8a4a 55%, #c0a662 80%, #a88f55 100%); }
  .hero-photo--desk { background: linear-gradient(120deg, #e9ebe8 0%, #d8dbd7 35%, #bfc2bd 60%, #6f6f6a 85%, #8a7a6a 100%); }

  .header-swoosh { position: absolute; left: 0; top: 0; width: 675px; height: 200px; }

  .brand { position: absolute; top: 36px; left: 0; width: 100%; text-align: center; }
  .brand__row { display: inline-flex; align-items: center; gap: 12px; }
  .brand__dot { width: 46px; height: 46px; border-radius: 50%; background: var(--green-dark); }
  .brand__name { font-family: "Rubik", sans-serif; font-weight: 500; font-size: 27px; color: var(--green-dark); letter-spacing: .5px; text-transform: uppercase; }
  .brand__tag { display: block; font-family: "Rubik", sans-serif; font-weight: 500; font-size: 9px; letter-spacing: 3px; color: var(--green-dark); margin: 2px 0 0 58px; }

  .title-box {
    position: absolute; left: 0; top: 330px; width: 336px; height: 154px;
    background: var(--green-dark); border-radius: 0 10px 10px 0;
    padding: 14px 0 0 56px;
    font-family: "Rubik", sans-serif; font-weight: 800; text-transform: uppercase; line-height: 1;
  }
  .title-box__line { display: block; color: var(--white); font-size: 43px; margin-bottom: 3px; }
  .title-box__accent { display: block; color: var(--green-light); font-size: 35px; margin-top: 4px; }
  .flyer--office .title-box { padding-left: 62px; }
  .flyer--office .title-box__line { font-size: 41px; }
  .flyer--office .title-box__accent { font-size: 28px; }

  .col-head { position: absolute; top: 512px; height: 29px; width: 260px; background: var(--green-light); color: var(--white); font-family: "Rubik", sans-serif; font-weight: 700; font-size: 18px; text-align: center; line-height: 29px; text-transform: uppercase; }
  .col-head--benefit { left: 56px; }
  .col-head--why { left: 360px; }

  .benefit-list { position: absolute; left: 56px; top: 558px; width: 270px; list-style: none; }
  .benefit { display: flex; gap: 12px; height: 68px; }
  .benefit svg { flex: none; width: 52px; height: 52px; }
  .benefit__title { font-family: "Rubik", sans-serif; font-weight: 700; font-size: 14.5px; color: var(--green-dark); }
  .benefit__text { font-size: 13px; line-height: 1.25; color: var(--ink-soft); }

  .tick-list { position: absolute; list-style: none; }
  .tick-list--why { left: 360px; top: 562px; width: 280px; }
  .tick { position: relative; padding-left: 20px; font-size: 12.5px; line-height: 1.3; color: var(--ink-soft); margin-bottom: 10px; }
  .tick::before { content: ""; position: absolute; left: 0; top: 4px; width: 10px; height: 10px; border-radius: 50%; background: var(--green-light); }
  .tick::after { content: ""; position: absolute; left: 3px; top: 6px; width: 3px; height: 5px; border: solid var(--white); border-width: 0 1.5px 1.5px 0; transform: rotate(45deg); }
  .tick-list--dark .tick::before { background: var(--green-dark); }

  .feature-row { position: absolute; left: 40px; top: 505px; width: 595px; display: flex; }
  .feature { flex: 1; text-align: center; padding: 0 10px; border-left: 1px solid #b9cf96; height: 145px; }
  .feature:first-child { border-left: none; }
  .feature svg { width: 58px; height: 58px; }
  .feature__title { font-family: "Rubik", sans-serif; font-weight: 700; font-size: 14px; color: var(--green-dark); margin-top: 10px; }
  .feature__text { font-size: 11.5px; line-height: 1.25; color: var(--ink-soft); margin-top: 4px; }

  .programs { position: absolute; left: 0; top: 665px; width: 675px; height: 180px; background: var(--green-pale); }
  .programs__intro { position: absolute; left: 62px; top: 22px; width: 250px; }
  .programs__title { font-family: "Rubik", sans-serif; font-weight: 800; font-size: 20px; line-height: 1.1; color: var(--green-dark); text-transform: uppercase; }
  .programs__title span { color: var(--green-light); display: block; }
  .programs__text { font-size: 13px; line-height: 1.3; color: var(--ink-soft); margin-top: 4px; }
  .programs .tick-list { left: 360px; top: 30px; width: 290px; }
  .programs .tick { margin-bottom: 16px; }

  .footer { position: absolute; left: 0; top: 845px; width: 675px; height: 110px; background: var(--green-dark); text-align: center; padding-top: 26px; }
  .footer__cta { font-family: "Rubik", sans-serif; font-weight: 700; font-size: 20px; color: var(--green-light); text-transform: uppercase; }
  .footer__contacts { display: flex; justify-content: center; align-items: center; gap: 9px; margin-top: 10px; font-size: 14.5px; color: var(--white); }
  .footer__contacts svg { width: 12px; height: 12px; vertical-align: -1px; margin-right: 4px; }
  .footer__sep { opacity: .8; }
</style>
</head>
<body>

<svg width="0" height="0" style="position:absolute">
  <defs>
    <symbol id="icon-cash-ring" viewBox="0 0 52 52">
      <circle cx="26" cy="26" r="24" fill="none" stroke="#a2c767" stroke-width="2"/>
      <circle cx="26" cy="26" r="14" fill="none" stroke="#a2c767" stroke-width="2.5"/>
      <text x="26" y="31" text-anchor="middle" font-family="Rubik, sans-serif" font-weight="700" font-size="14" fill="#a2c767">$</text>
    </symbol>
    <symbol id="icon-cash-badge" viewBox="0 0 58 58">
      <circle cx="29" cy="29" r="28" fill="#a2c767"/>
      <circle cx="29" cy="29" r="15" fill="none" stroke="#fff" stroke-width="2.5"/>
      <text x="29" y="34.5" text-anchor="middle" font-family="Rubik, sans-serif" font-weight="700" font-size="15" fill="#fff">$</text>
    </symbol>
    <symbol id="icon-web" viewBox="0 0 12 12"><circle cx="6" cy="6" r="5.5" fill="#fff"/><path d="M1 6h10M6 1c2.5 3 2.5 7 0 10M6 1c-2.5 3-2.5 7 0 10" stroke="#0f4a1e" fill="none" stroke-width=".9"/></symbol>
    <symbol id="icon-phone" viewBox="0 0 12 12"><circle cx="6" cy="6" r="5.5" fill="#fff"/><path d="M4 3.2l1 1.4-.6.8c.5 1 1.2 1.7 2.2 2.2l.8-.6 1.4 1-.6 1.1C6 9 3 6 3.1 3.8z" fill="#0f4a1e"/></symbol>
    <symbol id="icon-mail" viewBox="0 0 12 12"><circle cx="6" cy="6" r="5.5" fill="#fff"/><rect x="3" y="4" width="6" height="4.2" fill="none" stroke="#0f4a1e" stroke-width=".9"/><path d="M3 4l3 2.4L9 4" fill="none" stroke="#0f4a1e" stroke-width=".9"/></symbol>
    <symbol id="header-swoosh" viewBox="0 0 675 200">
      <path d="M0 0H675V30C520 125 250 160 0 42Z" fill="#fff"/>
      <path d="M0 42C250 160 520 125 675 30V78C520 170 240 190 0 92Z" fill="#a2c767"/>
      <path d="M0 70C240 160 500 150 675 60V64C500 158 240 168 0 76Z" fill="#cfe2ad"/>
      <path d="M290 158C470 150 600 90 675 30V72C590 125 460 168 290 158Z" fill="#0f4a1e"/>
    </symbol>
  </defs>
</svg>

<!-- Promotional template -->
<article class="flyer flyer--harvest">
  <div class="hero-photo hero-photo--field" role="img" aria-label="Photo of a forage harvester filling a trailer in a corn field"></div>
  <svg class="header-swoosh"><use href="#header-swoosh"/></svg>
  <div class="brand">
    <div class="brand__row"><span class="brand__dot"></span><div><span class="brand__name">Brightmoor Funding</span><span class="brand__tag">— EQUIPMENT FINANCE —</span></div></div>
  </div>
  <h1 class="title-box"><span class="title-box__line">Equipment</span><span class="title-box__line">Financing</span><span class="title-box__accent">Made Simple</span></h1>

  <h2 class="col-head col-head--benefit">Benefit</h2>
  <h2 class="col-head col-head--why">Why Choose Us?</h2>
  <ul class="benefit-list">
    <li class="benefit"><svg><use href="#icon-cash-ring"/></svg><div><p class="benefit__title">Preserve Cash Flow</p><p class="benefit__text">Lorem ipsum dolor sit amet, consectetur adipiscing elit.</p></div></li>
    <li class="benefit"><svg><use href="#icon-cash-ring"/></svg><div><p class="benefit__title">Preserve Cash Flow</p><p class="benefit__text">Lorem ipsum dolor sit amet, consectetur adipiscing elit.</p></div></li>
    <li class="benefit"><svg><use href="#icon-cash-ring"/></svg><div><p class="benefit__title">Preserve Cash Flow</p><p class="benefit__text">Lorem ipsum dolor sit amet, consectetur adipiscing elit.</p></div></li>
    <li class="benefit"><svg><use href="#icon-cash-ring"/></svg><div><p class="benefit__title">Preserve Cash Flow</p><p class="benefit__text">Lorem ipsum dolor sit amet, consectetur adipiscing elit.</p></div></li>
  </ul>
  <ul class="tick-list tick-list--why">
    <li class="tick">Lorem ipsum dolor sit amet, consectetur adipiscing elit, sed do eiusmod tempor</li>
    <li class="tick">Lorem ipsum dolor sit amet, consectetur adipiscing elit, sed do eiusmod tempor</li>
    <li class="tick">Lorem ipsum dolor sit amet, consectetur adipiscing elit, sed do eiusmod tempor</li>
    <li class="tick">Lorem ipsum dolor sit amet, consectetur adipiscing elit, sed do eiusmod tempor</li>
    <li class="tick">Lorem ipsum dolor sit amet, consectetur adipiscing elit, sed do eiusmod tempor</li>
    <li class="tick">Lorem ipsum dolor sit amet, consectetur adipiscing elit, sed do eiusmod tempor</li>
  </ul>

  <footer class="footer">
    <p class="footer__cta">Talk to a financing specialist today</p>
    <p class="footer__contacts">
      <span><svg><use href="#icon-web"/></svg>brightmoorfunding.com</span><span class="footer__sep">|</span>
      <span><svg><use href="#icon-phone"/></svg>hello@brightmoorfunding.com</span><span class="footer__sep">|</span>
      <span><svg><use href="#icon-mail"/></svg>(800) 555-0148</span>
    </p>
  </footer>
</article>

<!-- Educational template -->
<article class="flyer flyer--office">
  <div class="hero-photo hero-photo--desk" role="img" aria-label="Photo of a hand using a calculator beside a laptop and financial charts"></div>
  <svg class="header-swoosh"><use href="#header-swoosh"/></svg>
  <div class="brand">
    <div class="brand__row"><span class="brand__dot"></span><div><span class="brand__name">Brightmoor Funding</span><span class="brand__tag">— EQUIPMENT FINANCE —</span></div></div>
  </div>
  <h1 class="title-box"><span class="title-box__line">Get the</span><span class="title-box__line">Equipment</span><span class="title-box__accent">You Need Today</span></h1>

  <div class="feature-row">
    <div class="feature"><svg><use href="#icon-cash-badge"/></svg><p class="feature__title">Preserve Cash Flow</p><p class="feature__text">Lorem ipsum dolor sit amet, consectetur adipiscing elit, sed do eiusmod tempor incididunt ut labore et dolore</p></div>
    <div class="feature"><svg><use href="#icon-cash-badge"/></svg><p class="feature__title">Preserve Cash Flow</p><p class="feature__text">Lorem ipsum dolor sit amet, consectetur adipiscing elit, sed do eiusmod tempor incididunt ut labore et dolore</p></div>
    <div class="feature"><svg><use href="#icon-cash-badge"/></svg><p class="feature__title">Preserve Cash Flow</p><p class="feature__text">Lorem ipsum dolor sit amet, consectetur adipiscing elit, sed do eiusmod tempor incididunt ut labore et dolore</p></div>
  </div>

  <section class="programs">
    <div class="programs__intro">
      <h2 class="programs__title">Special Financing<br>Programs for<span>Qualified Businesses</span></h2>
      <p class="programs__text">Lorem ipsum dolor sit amet, consectetur dipiscing elit, sed do eiusmod tempor incididunt ut labore et dolore magna aliqua.</p>
    </div>
    <ul class="tick-list tick-list--dark">
      <li class="tick">Lorem ipsum dolor sit amet, consectetur adipiscing elit, sed do eiusmod tempor</li>
      <li class="tick">Lorem ipsum dolor sit amet, consectetur adipiscing elit, sed do eiusmod tempor</li>
      <li class="tick">Lorem ipsum dolor sit amet, consectetur adipiscing elit, sed do eiusmod tempor</li>
    </ul>
  </section>

  <footer class="footer">
    <p class="footer__cta">Talk to a financing specialist today</p>
    <p class="footer__contacts">
      <span><svg><use href="#icon-web"/></svg>brightmoorfunding.com</span><span class="footer__sep">|</span>
      <span><svg><use href="#icon-phone"/></svg>hello@brightmoorfunding.com</span><span class="footer__sep">|</span>
      <span><svg><use href="#icon-mail"/></svg>(800) 555-0148</span>
    </p>
  </footer>
</article>

</body>
</html>
```